Semaglutide Diet

A flyer design for a weight loss program based on the peptide Semaglutide that our clinic is rolling out. Here are some very rough ideas

```html
<!DOCTYPE html>
<html lang="en">
<head>
<meta charset="utf-8">
<title>Semaglutide Diet Flyer</title>
<link rel="stylesheet" href="https://fonts.googleapis.com/css2?family=Anton&family=Arimo:wght@400;700&display=swap">
<style>
  :root {
    --page-bg: #e9e7e4;
    --ink-black: #1e1e1e;
    --brand-blue: #344b9b;
    --brand-red: #e20a17;
    --band-grey: #b6b6b8;
    --body-grey: #ecedef;
    --text-dark: #262626;
    --white: #ffffff;
    --shadow: #17172a;
  }
  * { margin: 0; padding: 0; box-sizing: border-box; }
  html, body { width: 1200px; height: 1200px; overflow: hidden; background: var(--page-bg); }
  .flyer {
    position: absolute; left: 137px; top: 0;
    width: 926px; height: 1200px;
    font-family: "Arimo", Arial, sans-serif;
    color: var(--text-dark);
    overflow: hidden;
  }
  .flyer-shapes { position: absolute; inset: 0; }
  .display { font-family: "Anton", "Impact", sans-serif; }
  .tab-title {
    position: absolute; top: 756px; height: 50px;
    line-height: 52px; color: var(--white);
    font-weight: 700; font-size: 29px; letter-spacing: 0.3px;
  }
  .tab-title.want { left: 56px; }
  .tab-title.drug { left: 532px; }
  .benefit-list { position: absolute; left: 38px; top: 823px; list-style: none; }
  .benefit-list li {
    position: relative; padding-left: 31px;
    font-size: 29px; height: 57.5px; line-height: 38px;
  }
  .benefit-list li::before {
    content: ""; position: absolute; left: 2px; top: 18px;
    width: 9px; height: 9px; border-radius: 50%; background: var(--text-dark);
  }
  .approval-note {
    position: absolute; left: 533px; top: 816px;
    font-size: 14px; font-weight: 700; letter-spacing: 0.1px;
  }
  .program-list { position: absolute; left: 511px; top: 838px; list-style: none; }
  .program-list li {
    position: relative; padding-left: 20px;
    font-size: 20px; line-height: 22px; margin-bottom: 8px; letter-spacing: 0.2px;
  }
  .program-list li::before {
    content: ""; position: absolute; left: 3px; top: 10px;
    width: 5px; height: 5px; border-radius: 50%; background: var(--text-dark);
  }
  .pricing {
    position: absolute; left: 511px; top: 1071px; width: 390px;
    font-size: 17px; line-height: 22px;
  }
  .pricing strong { font-weight: 700; }
  .contact-phone {
    position: absolute; left: 16px; top: 1133px;
    font-size: 34px; font-weight: 700; color: var(--white); letter-spacing: 0.4px;
  }
  .contact-email {
    position: absolute; left: 432px; top: 1141px;
    font-size: 28px; font-weight: 700; color: var(--white); letter-spacing: 0.3px;
  }
</style>
</head>
<body>
<main class="flyer">
  <svg class="flyer-shapes" viewBox="0 0 926 1200" width="926" height="1200" xmlns="http://www.w3.org/2000/svg">
    <defs>
      <linearGradient id="heroTone" x1="0" y1="0" x2="1" y2="1">
        <stop offset="0" stop-color="#f2f2f4"/>
        <stop offset="1" stop-color="#e3d6cd"/>
      </linearGradient>
      <linearGradient id="gymTone" x1="0" y1="0" x2="1" y2="1">
        <stop offset="0" stop-color="#f1f2f4"/>
        <stop offset="0.5" stop-color="#e4e5e8"/>
        <stop offset="1" stop-color="#eeeff1"/>
      </linearGradient>
    </defs>

    <g role="img" aria-label="Photo of a fit woman in a sports top measuring her waist with a tape">
      <rect x="300" y="0" width="626" height="663" fill="url(#heroTone)"/>
    </g>
    <g role="img" aria-label="Faded background photo of a person training in a gym">
      <rect x="0" y="743" width="926" height="378" fill="url(#gymTone)"/>
    </g>

    <polygon class="logo-block" points="0,0 470,0 310,214 0,214" fill="var(--ink-black)"/>
    <polygon class="accent-stripe" points="470,0 497,0 337,214 310,214" fill="var(--brand-red)"/>
    <polygon class="hero-chevron" points="0,214 333,214 550,485 345,743 0,743" fill="var(--brand-blue)"/>
    <polygon class="accent-corner" points="460,600 510,663 445,743 345,743" fill="var(--brand-red)"/>
    <polygon class="grey-band" points="510,663 926,663 926,743 445,743" fill="var(--band-grey)"/>

    <polygon class="tab-want" points="37,756 300,756 332,806 37,806" fill="var(--brand-blue)"/>
    <polygon class="tab-drug" points="513,756 775,756 808,806 513,806" fill="var(--brand-blue)"/>

    <polygon class="footer-phone" points="0,1121 367,1121 420,1200 0,1200" fill="var(--brand-blue)"/>
    <polygon class="footer-email" points="367,1121 926,1121 926,1200 420,1200" fill="var(--brand-red)"/>

    <g class="display" fill="var(--white)" font-size="64">
      <text x="31" y="90" textLength="268" lengthAdjust="spacingAndGlyphs">YOUR LOGO</text>
      <text x="31" y="163" textLength="120" lengthAdjust="spacingAndGlyphs">HERE</text>
    </g>

    <g class="display headline" font-size="118">
      <g fill="var(--shadow)" transform="translate(6,4)">
        <text x="23" y="375" textLength="295" lengthAdjust="spacingAndGlyphs">DO YOU</text>
        <text x="23" y="535" textLength="240" lengthAdjust="spacingAndGlyphs">WANT</text>
        <text x="23" y="690" textLength="345" lengthAdjust="spacingAndGlyphs">RESULT?</text>
      </g>
      <g fill="var(--white)">
        <text x="23" y="375" textLength="295" lengthAdjust="spacingAndGlyphs">DO YOU</text>
        <text x="23" y="535" textLength="240" lengthAdjust="spacingAndGlyphs">WANT</text>
        <text x="23" y="690" textLength="345" lengthAdjust="spacingAndGlyphs">RESULT?</text>
      </g>
    </g>
  </svg>

  <h2 class="tab-title want">DO YOU WANT?</h2>
  <ul class="benefit-list">
    <li>Lose 5 pounds or more</li>
    <li>Improve your metabolism</li>
    <li>Have more energy</li>
    <li>Lose water weight</li>
    <li>Improve overall health</li>
  </ul>

  <h2 class="tab-title drug">SEMAGLUTIIDE</h2>
  <p class="approval-note">(FDA APPROVED SLIMVEX/GLUVORA)</p>
  <ul class="program-list">
    <li>Physician Weight Loss Program</li>
    <li>Up to 2-4 pounds per Week</li>
    <li>Reduces Appetite,<br>Improves cravings Burns</li>
    <li>Fat and Boosts Energy</li>
    <li>Reverses Insulin Resistance</li>
    <li>Safe and Effective</li>
    <li>Once Weekly Injection</li>
  </ul>
  <p class="pricing"><strong>PRICING INCLUDES:</strong> Semglutide, Liptropic<br>Fat buring B-12 , and Supplies</p>

  <p class="contact-phone">Ph.No. : 0123 456789</p>
  <p class="contact-email">Email : yourname@website.com</p>
</main>
</body>
</html>
```